***PLASTIC*** Business Card Design

1 sided business card design
The card will be screen printed on plastic, so colour and fonts must be strong.

Must use the colours in the logo eps attached (Black/Ivory/White). Other colour(s) can be added.

Four (4) examples of how the logo can be printed are included in the logo eps attached.

The business card should highlight the logo. The card will be given to architects, interior designers and builders. It should look sophisticated but also innovative.

Do not cover the whole card with colour as it is important than some of the frosted plastic card is visible.

Be creative.

Target Market(s)

architects, interior designers and builders and wealthy home owners

Industry/Entity Type

Plastic

Requirements
Must have
• Must use the colours in the logo eps attached (Black/Ivory/White). Other colour(s) can be added if necessary.

The font is Square721 ExBT but has been a little thickened. It is not essential that you use this font. The name should be a stronger version of the font than other details.

The card will be printed on PVC - see http://www.voltrap.com.au/pricelistbcardsplastic.php

Final artwork must be print ready. You must use the printing spec at http://www.voltrap.com.au/2011%20PVC-TW.pdf

The actual details to be typeset ono the card are:

Dorian Welch

Mobile: 0412 806133
email: info@halcoworks.com.au
www.halcoworks.com.au

PO Box 53, Altona, Vic 3018

Plastering | Rendering | Cornicing

```html
<!DOCTYPE html>
<html lang="en">
<head>
<meta charset="utf-8">
<title>Halco Works – Business Card</title>
<link rel="stylesheet" href="https://fonts.googleapis.com/css2?family=Mulish:wght@400;700;800&display=swap">
<style>
  :root {
    --backdrop: #5c5c5c;
    --frost-top: #bdbdbd;
    --frost-bottom: #a9a9a9;
    --ink: #111111;
    --ink-soft: #1c1c1c;
    --band: #0c0c0c;
    --band-text: #f4f1e8;
  }
  * { margin: 0; padding: 0; box-sizing: border-box; }
  html, body {
    width: 1200px;
    height: 720px;
    overflow: hidden;
    background: var(--backdrop);
  }
  .stage {
    width: 1200px;
    height: 720px;
    display: flex;
    align-items: center;
    justify-content: center;
  }
  .card {
    position: relative;
    width: 374px;
    height: 634px;
    background: linear-gradient(180deg, var(--frost-top), var(--frost-bottom));
    color: var(--ink);
    font-family: "Mulish", "Helvetica Neue", Arial, sans-serif;
    text-align: center;
  }
  .brand {
    position: absolute;
    top: 64px;
    left: 0;
    right: 0;
    font-family: "Mulish", "Helvetica Neue", Arial, sans-serif;
    font-weight: 800;
    color: var(--ink);
    line-height: 1;
  }
  .brand-main {
    display: block;
    font-size: 56px;
    letter-spacing: 3px;
  }
  .brand-sub {
    display: block;
    margin-top: 8px;
    font-size: 22px;
    letter-spacing: 6px;
  }
  .holder-name {
    position: absolute;
    top: 230px;
    left: 0;
    right: 0;
    font-weight: 700;
    font-size: 21px;
    letter-spacing: 0.5px;
    color: var(--ink-soft);
  }
  .contact {
    position: absolute;
    top: 380px;
    left: 0;
    right: 0;
    list-style: none;
    font-size: 19px;
    line-height: 32px;
    color: var(--ink-soft);
  }
  .services {
    position: absolute;
    top: 541px;
    left: 0;
    right: 0;
    height: 30px;
    background: var(--band);
    color: var(--band-text);
    font-size: 16px;
    line-height: 30px;
    letter-spacing: 0.3px;
  }
  .website {
    position: absolute;
    top: 590px;
    left: 0;
    right: 0;
    font-size: 19px;
    letter-spacing: 0.5px;
    color: var(--ink-soft);
  }
</style>
</head>
<body>
  <main class="stage">
    <article class="card">
      <h1 class="brand">
        <span class="brand-main">HALCO</span>
        <span class="brand-sub">WORKS</span>
      </h1>
      <p class="holder-name">Dorian Welch</p>
      <ul class="contact">
        <li class="contact-phone">041.280.6133</li>
        <li class="contact-address">PO Box 53, Carrow, Vic 3921</li>
        <li class="contact-email">info@halcoworks.com.au</li>
      </ul>
      <p class="services">Plastering | Rendering | Cornicing</p>
      <p class="website">www.halcoworks.com.au</p>
    </article>
  </main>
</body>
</html>
```